TAILWIND FIELDS Pet Resorts Outdoor Signage

4 x 8 outdoor signage design for our two locations

Target Market(s)

Existing and New Customers

Industry/Entity Type

Pet Care

Font styles to use
Sans Serif

Colors

Designer to choose colors to be used in the design.

```html
<!DOCTYPE html>
<html lang="en">
<head>
<meta charset="utf-8">
<title>Tailwind Fields Pet Resorts – Outdoor Sign</title>
<link rel="stylesheet" href="https://fonts.googleapis.com/css2?family=Oswald:wght@600;700&family=Arimo:wght@400;700&display=swap">
<style>
  :root {
    --page-bg: #f2f2f0;
    --navy: #302c4c;
    --teal: #22a7a7;
    --teal-deep: #3a8da0;
    --amber: #f9b142;
    --panel-white: #ffffff;
    --ink-grey: #444446;
    --white: #ffffff;
  }
  html, body {
    margin: 0;
    width: 1200px;
    height: 1200px;
    overflow: hidden;
    background: var(--page-bg);
  }
  .canvas {
    width: 1200px;
    height: 1200px;
    display: flex;
    align-items: center;
    justify-content: center;
  }
  .sign {
    width: 1120px;
    height: 560px;
    display: block;
    box-shadow: 0 10px 30px rgba(0,0,0,0.15);
  }
  .headline { font-family: "Oswald", "Arial Narrow", sans-serif; font-weight: 700; fill: var(--teal-deep); }
  .tagline { font-family: "Arimo", Arial, sans-serif; font-weight: 400; fill: var(--white); }
  .service { font-family: "Arimo", Arial, sans-serif; font-weight: 700; fill: var(--navy); }
  .phone { font-family: "Oswald", "Arial Narrow", sans-serif; font-weight: 700; fill: var(--amber); }
  .web { font-family: "Arimo", Arial, sans-serif; font-weight: 400; fill: var(--teal); }
  .brand-name { font-family: "Arimo", Arial, sans-serif; font-weight: 700; fill: var(--ink-grey); }
  .icon-disc { fill: var(--navy); }
  .icon-bar { fill: var(--amber); }
  .bg-white { fill: var(--panel-white); }
  .bg-navy { fill: var(--navy); }
  .bg-amber { fill: var(--amber); }
  .bg-teal { fill: var(--teal); }
  .brand-dot { fill: var(--teal); }
</style>
</head>
<body>
<main class="canvas">
  <svg class="sign" viewBox="0 0 1040 520" xmlns="http://www.w3.org/2000/svg" aria-label="Tailwind Fields Pet Resorts outdoor sign">
    <!-- base panels -->
    <rect class="bg-navy" x="0" y="0" width="1040" height="520"/>
    <rect class="bg-amber" x="380" y="195" width="660" height="142"/>
    <path class="bg-teal" d="M0 0 H330 Q415 0 415 95 L350 520 H0 Z"/>
    <path class="bg-white" d="M0 0 H330 Q405 0 400 90 L318 520 H0 Z"/>

    <!-- brand block -->
    <circle class="brand-dot" cx="60" cy="120" r="26"/>
    <text class="brand-name" x="30" y="230" font-size="58">TAILWIND</text>
    <text class="brand-name" x="30" y="298" font-size="58">FIELDS</text>

    <!-- headline -->
    <text class="headline" x="472" y="102" font-size="92" letter-spacing="1">PET RESORT</text>
    <text class="tagline" x="468" y="168" font-size="52">All Breed Friendly</text>

    <!-- services, column one -->
    <g class="service-item">
      <circle class="icon-disc" cx="510" cy="224" r="11"/><rect class="icon-bar" x="503" y="222" width="14" height="4" rx="2"/>
      <text class="service" x="535" y="231" font-size="19">BOARDING</text>
    </g>
    <g class="service-item">
      <circle class="icon-disc" cx="510" cy="269" r="11"/><rect class="icon-bar" x="503" y="267" width="14" height="4" rx="2"/>
      <text class="service" x="535" y="276" font-size="19">DAYCARE</text>
    </g>
    <g class="service-item">
      <circle class="icon-disc" cx="510" cy="314" r="11"/><rect class="icon-bar" x="503" y="312" width="14" height="4" rx="2"/>
      <text class="service" x="535" y="321" font-size="19">TRAINING FULL</text>
    </g>

    <!-- services, column two -->
    <g class="service-item">
      <circle class="icon-disc" cx="736" cy="224" r="11"/><rect class="icon-bar" x="729" y="222" width="14" height="4" rx="2"/>
      <text class="service" x="758" y="231" font-size="19">SERVICE SALON</text>
    </g>
    <g class="service-item">
      <circle class="icon-disc" cx="736" cy="269" r="11"/><rect class="icon-bar" x="729" y="267" width="14" height="4" rx="2"/>
      <text class="service" x="758" y="276" font-size="19">PET TAXI</text>
    </g>
    <g class="service-item">
      <circle class="icon-disc" cx="736" cy="314" r="11"/><rect class="icon-bar" x="729" y="312" width="14" height="4" rx="2"/>
      <text class="service" x="758" y="321" font-size="19">Many more....</text>
    </g>

    <!-- contact -->
    <text class="phone" x="700" y="432" font-size="64" text-anchor="middle">905-555-0142</text>
    <text class="web" x="700" y="476" font-size="36" text-anchor="middle">www.tailwindfields.ca</text>
  </svg>
</main>
</body>
</html>
```